Venture firm needs flyer to attract Sales Professionals as Advisors

Creation of either a pdf Flyer or Brochure.
The target audience are senior sales professionals of the Information Technology industry. The flyer needs to come across highly professional, business oriented, positive. Text for the brochure is attached. The colors/graphics should align with Brindmore Capital corporate appearance: www.brindmore.capital

Target Market(s)

Sales Professionals in the Information Technology Industry

Industry/Entity Type

Information Technology

Font styles to use
• Raleway

Requirements
Must have
• fitting the corporate look and feel: www.brindmore.capital

```html
<!DOCTYPE html>
<html lang="en">
<head>
<meta charset="utf-8">
<title>Brindmore Capital – Achieving Growth Brochure</title>
<link rel="stylesheet" href="https://fonts.googleapis.com/css2?family=Oswald:wght@600&family=Raleway:wght@300;400;600&display=swap">
<style>
  :root {
    --navy: #1c3a5e;
    --navy-deep: #142c49;
    --accent: #6f9bc8;
    --paper: #ffffff;
    --ink: #3b4654;
    --ink-soft: #7a8593;
    --stage: #e3e4e6;
    --snow-light: #eef1f5;
    --snow-mid: #b9c4d2;
    --snow-dark: #6f7f95;
  }
  * { box-sizing: border-box; margin: 0; padding: 0; }
  html, body { width: 1200px; height: 1200px; overflow: hidden; }
  body { background: var(--stage); font-family: "Raleway", sans-serif; color: var(--ink); position: relative; }

  /* ---------- Cover ---------- */
  .cover {
    position: absolute; left: 220px; top: 30px; width: 760px; height: 440px;
    background: var(--navy); box-shadow: 0 6px 18px rgba(0,0,0,.18);
  }
  .cover__brand {
    position: absolute; top: 32px; width: 100%; text-align: center;
    font-weight: 300; font-size: 40px; letter-spacing: 2px; color: #e7eef6;
  }
  .cover__rule { position: absolute; left: 0; width: 100%; height: 6px; background: #dfe4ea; }
  .cover__rule--top { top: 100px; }
  .cover__rule--bottom { top: 346px; }
  .cover__photo {
    position: absolute; left: 0; top: 106px; width: 100%; height: 240px;
    background: linear-gradient(160deg, #8494aa 0%, var(--snow-light) 40%, #cdd6e2 65%, #8191a8 100%);
  }
  .cover__headline {
    position: absolute; left: 40px; top: 160px;
    font-family: "Oswald", sans-serif; font-weight: 600; font-size: 46px;
    letter-spacing: 1px; color: #ffffff; text-shadow: 0 2px 4px rgba(0,0,0,.35);
  }
  .cover__subline {
    position: absolute; left: 42px; top: 222px;
    font-weight: 600; font-size: 16px; color: #ffffff; text-shadow: 0 1px 3px rgba(0,0,0,.4);
  }

  /* ---------- Spreads ---------- */
  .spread {
    position: absolute; background: var(--paper); overflow: hidden;
    font-size: var(--fs); box-shadow: 0 5px 14px rgba(0,0,0,.16);
  }
  .spread--intl   { left: 30px;  top: 510px; width: 555px; height: 200px; --fs: 6px; }
  .spread--team   { left: 615px; top: 510px; width: 555px; height: 200px; --fs: 6px; }
  .spread--growth { left: 30px;  top: 745px; width: 1140px; height: 410px; --fs: 11px; }

  .spread__band-top { position: absolute; top: 0; left: 0; width: 100%; height: 8%; background: var(--navy); }
  .spread__band-bottom { position: absolute; bottom: 0; left: 0; width: 100%; height: 12%; background: var(--navy); border-top: 0.3em solid var(--accent); }
  .spread__gutter { position: absolute; top: 0; left: 49.6%; width: 0.8%; height: 100%; background: linear-gradient(90deg, rgba(0,0,0,0), rgba(0,0,0,.18), rgba(0,0,0,0)); z-index: 5; }
  .spread__footer {
    position: absolute; bottom: 4%; font-size: 1.4em; font-weight: 400;
    letter-spacing: .08em; color: #c9d6e6; text-transform: uppercase; z-index: 6;
  }
  .spread__footer--left { left: 2.5%; }
  .spread__footer--right { right: 2.5%; }

  .photo { position: absolute; top: 8%; height: 80%; }
  .panel { position: absolute; top: 8%; height: 80%; background: rgba(255,255,255,.93); padding: 3em 2em 0; }

  .heading { font-weight: 300; font-size: 1.7em; text-transform: uppercase; color: var(--ink); line-height: 1.1; }
  .subheading { font-weight: 400; font-size: 1.3em; text-transform: uppercase; color: var(--ink); margin-bottom: .8em; }
  .copy { font-size: .95em; line-height: 1.5; color: var(--ink-soft); margin-bottom: .9em; }

  /* intl spread */
  .intl__photo-left { left: 0; width: 24%; background: linear-gradient(180deg, #c3ccd8 0%, var(--snow-light) 45%, #f4f6f9 100%); }
  .intl__label { position: absolute; left: 2.3%; top: 22%; z-index: 3; }
  .intl__panel { left: 24%; width: 26%; }
  .intl__photo-right { left: 50%; width: 50%; background: linear-gradient(90deg, #f1e6e6 0%, #d8c6c8 45%, #a9a7b0 70%, #8b96a6 100%); }
  .intl__panel-right { left: 50%; width: 26%; background: rgba(255,255,255,.78); }

  /* team spread */
  .team__photo-left { left: 0; width: 29%; background: linear-gradient(180deg, #7fa7d6 0%, #b9cde6 40%, #eef2f7 70%, #ffffff 100%); }
  .team__panel { left: 29%; width: 21%; }
  .team__photo-right { left: 50%; width: 50%; background: linear-gradient(90deg, #b45a4b 0%, #d79d77 25%, #c9d3b8 50%, #f3f4f5 80%, #ffffff 100%); }
  .contact { position: absolute; right: 3%; top: 18%; width: 24%; }
  .contact__title { font-size: 1.3em; font-weight: 400; text-transform: uppercase; text-align: center; margin-bottom: 1.4em; }
  .contact__block { display: flex; gap: .6em; margin-bottom: 2em; align-items: flex-start; }
  .contact__text { width: 50%; font-size: .85em; line-height: 1.45; color: var(--ink-soft); text-align: right; }
  .contact__region { color: var(--accent); font-weight: 600; text-transform: uppercase; text-align: center; display: block; }
  .contact__map { width: 50%; height: 4em; background: linear-gradient(135deg, #eef0f3, #d7dce3); border: .12em solid #c9ced6; }

  /* growth spread */
  .growth__photo-left { left: 0; width: 24%; background: linear-gradient(180deg, #f5f6f8 0%, #e4e8ee 45%, #9aa3b0 75%, #eef0f3 100%); }
  .growth__label { position: absolute; left: 2.3%; top: 50%; z-index: 3; font-size: 1.5em; }
  .growth__panel { left: 24%; width: 26%; padding-top: 5em; }
  .growth__panel .subheading { font-size: 1.15em; margin-top: 1em; }
  .growth__rule { height: .15em; background: var(--navy); width: 80%; margin: -.3em 0 .8em; }
  .growth__photo-right { left: 50%; width: 50%; background: linear-gradient(100deg, #ffffff 0%, #eef1f5 40%, #c3cfdd 65%, #8a7a6a 85%, #6f6258 100%); }
  .growth__text { position: absolute; left: 53%; top: 16%; width: 25%; z-index: 3; }
  .growth__text .heading { margin-bottom: 1em; }
</style>
</head>
<body>

<section class="cover">
  <div class="cover__brand">BRINDMORE CAPITAL</div>
  <div class="cover__rule cover__rule--top"></div>
  <div class="cover__photo" role="img" aria-label="Mountaineer in a bright jacket standing on a snowy glacier summit"></div>
  <h1 class="cover__headline">ACHIEVING GROWTH</h1>
  <p class="cover__subline">Investing in Global Go-to-Market Strategies</p>
  <div class="cover__rule cover__rule--bottom"></div>
</section>

<section class="spread spread--intl">
  <div class="spread__band-top"></div>
  <div class="photo intl__photo-left" role="img" aria-label="Lone skier crossing a snowy mountain slope"></div>
  <h2 class="heading intl__label">Expand<br>Internationally</h2>
  <div class="panel intl__panel">
    <h3 class="subheading">Brindmore Sales Council (BSC)</h3>
    <p class="copy">The BSC is an invitation only global community of senior sales leaders. Members gain early access to new ventures and advisory roles.</p>
    <p class="copy">BSC members collaborate with each other to share trends, opportunities and advice with customers.</p>
    <p class="copy">Members gain visibility into the latest technologies and help solve complex business objectives.</p>
  </div>
  <div class="photo intl__photo-right" role="img" aria-label="Race car pit stop with crew in motion blur"></div>
  <div class="panel intl__panel-right">
    <h3 class="subheading">How it works:</h3>
    <p class="copy">BSC members are introduced to portfolio companies and stay up to date with industry trends and emerging technologies.</p>
    <p class="copy">Once exposed to a specific vendor members can decide if they would like to get further involved.</p>
  </div>
  <div class="spread__gutter"></div>
  <div class="spread__band-bottom"></div>
  <span class="spread__footer spread__footer--left">Brindmore Capital</span>
  <span class="spread__footer spread__footer--right">Brindmore Capital</span>
</section>

<section class="spread spread--team">
  <div class="spread__band-top"></div>
  <div class="photo team__photo-left" role="img" aria-label="Two hikers with poles walking across snow under a blue sky"></div>
  <div class="panel team__panel">
    <h3 class="subheading">Our Team</h3>
    <p class="copy">The people of Brindmore Capital are all seasoned executives of technology businesses. We know when to look for a new sales and marketing organization and how to build a performance culture.</p>
    <p class="copy">With Brindmore as an investment partner you get a reliable go-to-market engine.</p>
  </div>
  <div class="photo team__photo-right" role="img" aria-label="City skyline with palm trees fading into white"></div>
  <div class="contact">
    <h3 class="contact__title">Contact us:</h3>
    <div class="contact__block">
      <p class="contact__text"><span class="contact__region">USA</span>120 Harbor Street<br>Lakeview, CA 94000<br>info@brindmore.capital<br>Tel +1 555 010 2040</p>
      <div class="contact__map" role="img" aria-label="Location map of the USA office"></div>
    </div>
    <div class="contact__block">
      <p class="contact__text"><span class="contact__region">Europe</span>Lindenweg 12<br>10115 Berlin, Germany<br>office@brindmore.capital<br>Tel +49 30 5550 1200</p>
      <div class="contact__map" role="img" aria-label="Location map of the Europe office"></div>
    </div>
  </div>
  <div class="spread__gutter"></div>
  <div class="spread__band-bottom"></div>
  <span class="spread__footer spread__footer--left">Brindmore Capital</span>
  <span class="spread__footer spread__footer--right">Brindmore Capital</span>
</section>

<section class="spread spread--growth">
  <div class="spread__band-top"></div>
  <div class="photo growth__photo-left" role="img" aria-label="Skier carving through powder snow"></div>
  <h2 class="heading growth__label">Improve productivity<br>with velocity sales</h2>
  <div class="panel growth__panel">
    <h3 class="subheading">As Associates:</h3>
    <p class="copy">Associates work with portfolio companies on defined sales projects and share in the success.</p>
    <div class="growth__rule"></div>
    <h3 class="subheading">As Advisors:</h3>
    <p class="copy">Advisors guide leadership teams on strategy, channels and hiring for growth.</p>
    <div class="growth__rule"></div>
  </div>
  <div class="photo growth__photo-right" role="img" aria-label="Climber reaching down to help a partner up a rock summit"></div>
  <div class="growth__text">
    <h2 class="heading">Leverage<br>channel and<br>technology partners</h2>
    <p class="copy">Brindmore companies gain access to an experienced network of channel and technology partners worldwide. Together we build alliances that open new markets quickly.</p>
  </div>
  <div class="spread__gutter"></div>
  <div class="spread__band-bottom"></div>
  <span class="spread__footer spread__footer--left">Brindmore Capital</span>
  <span class="spread__footer spread__footer--right">Brindmore Capital</span>
</section>

</body>
</html>
```